Young Accounting firm needing a captivating business card

We need a business card design that forces the person to look at the card because its either gold foil, plastic, or lettering pop up etc. We already have a logo with a specific gold color and we need to make it pop. We are an accounting firm. I need the words" accounting, payroll, licenses, audits, taxes" somewhere on the business card so as to describe what we do- preferably on the side where the logo is at.

Industry/Entity Type

Accounting

Contact Information for Business Card

Address 48276 9th Ave S Ste 305, Alder Bay, OR 97405
Business Phone (541)418-2096
Fax (360)418-2157
Office Cell Phone (360)586-7319

Font styles to use
Serif

Colors
85abd2

Requirements
Must have
• It should state
• "Accounting" "Taxes" "Audits" "Licenses" "Payroll"
Nice to have
• Matte with gold foil, different textures, With Either a textured ivory background or gray blue slate background
Should not have
• colorful colors

```html
<!DOCTYPE html>
<html lang="en">
<head>
<meta charset="utf-8">
<title>Corvell Tax — Business Card</title>
<link rel="stylesheet" href="https://fonts.googleapis.com/css2?family=Source+Sans+3:wght@400;600&display=swap">
<style>
  :root {
    --backdrop: #e2e1e2;
    --gold-light: #cfa747;
    --gold-mid: #c39a3c;
    --gold-deep: #b08a3c;
    --gold-ink: #a9862f;
    --gold-raised: #d6b567;
    --card-white: #eceeee;
    --card-shade: #dfe1e1;
  }
  * { box-sizing: border-box; margin: 0; padding: 0; }
  html, body { width: 1200px; height: 1200px; overflow: hidden; }
  body {
    background: var(--backdrop);
    font-family: "Source Sans 3", sans-serif;
    position: relative;
  }
  .card {
    position: absolute;
    left: 300px;
    width: 600px;
    height: 343px;
  }
  .card-front {
    top: 207px;
    background: linear-gradient(135deg, var(--gold-deep) 0%, var(--gold-light) 40%, var(--gold-mid) 65%, var(--gold-deep) 100%);
    display: flex;
    align-items: center;
    justify-content: center;
  }
  .card-back {
    top: 650px;
    background: linear-gradient(135deg, var(--card-white), var(--card-shade));
    color: var(--gold-ink);
  }
  .brand {
    display: flex;
    align-items: center;
    gap: 12px;
    font-weight: 600;
    letter-spacing: 0.5px;
  }
  .brand-square { display: block; }
  .card-front .brand { color: var(--gold-raised); font-size: 54px; }
  .card-front .brand-square { width: 40px; height: 40px; background: var(--gold-raised); }
  .card-back .brand {
    position: absolute;
    left: 0; right: 0; top: 62px;
    justify-content: center;
    font-size: 38px;
  }
  .card-back .brand-square { width: 28px; height: 28px; background: var(--gold-ink); }
  .contact-line {
    position: absolute;
    display: flex;
    align-items: center;
    gap: 10px;
    font-size: 12px;
    font-weight: 400;
    text-transform: uppercase;
    line-height: 1.25;
  }
  .contact-line svg { width: 14px; height: 14px; flex: none; fill: var(--gold-ink); }
  .office { right: 34px; top: 140px; text-align: right; }
  .phone { right: 34px; top: 182px; }
  .email { left: 40px; top: 222px; }
  .web { left: 40px; top: 250px; letter-spacing: 2px; }
  .services {
    position: absolute;
    left: 0; right: 0; bottom: 30px;
    text-align: center;
    font-size: 19px;
    letter-spacing: 1.5px;
  }
</style>
</head>
<body>
  <section class="card card-front" aria-label="Card front">
    <div class="brand"><span class="brand-square"></span>Corvell Tax</div>
  </section>

  <section class="card card-back" aria-label="Card back">
    <div class="brand"><span class="brand-square"></span>Corvell Tax</div>

    <div class="contact-line office">
      <span>Address 48276 9th Ave S Ste 305<br>Alder Bay, OR 97405</span>
      <svg viewBox="0 0 16 16"><path d="M8 1 1 7.5h2V15h4v-4h2v4h4V7.5h2z"/></svg>
    </div>
    <div class="contact-line phone">
      <span>(541)418-2096</span>
      <svg viewBox="0 0 16 16"><path d="M3.6 1.5 6 4c.4.4.4 1 0 1.4L5 6.5c.8 1.8 2.5 3.5 4.5 4.5l1.1-1c.4-.4 1-.4 1.4 0l2.5 2.4c.4.4.4 1 0 1.4l-1.2 1.2C9.4 15.4.6 6.6 1.2 2.7L2.2 1.5c.4-.4 1-.4 1.4 0z"/></svg>
    </div>

    <div class="contact-line email">
      <span>brand_name@email.com</span>
      <svg viewBox="0 0 16 16"><path d="M1 3h14v10H1zm1.5 1.2L8 8.6l5.5-4.4z"/></svg>
    </div>
    <div class="contact-line web">
      <span>www.brandname.com</span>
      <svg viewBox="0 0 16 16"><circle cx="3" cy="13" r="1.8"/><path d="M2 8a6 6 0 0 1 6 6H6.3A4.3 4.3 0 0 0 2 9.7zm0-5a11 11 0 0 1 11 11h-1.7A9.3 9.3 0 0 0 2 4.7z"/></svg>
    </div>

    <p class="services">Accounting • Taxes • Audits • Licenses • Payroll</p>
  </section>
</body>
</html>
```